Word Bureau Ostrelle Templates

We run a large number of businesses, including schools, airports, hotels and offices. We write reports on a daily basis and are looking for a strong and sexy WORD Template. We already have a logo in place (see graphical chart attached), that is rights' protected. We are looking for a beautiful wich reflect modern design and human aspects. Our logo has 2 design, full fill and watermark. It can be used in red or black.

Architects, Fire brigade, Building investors, contactors

• Arial, Calibri, ...

• Cover page, summary, Bullet points, Tables, Figures, Annex

```html
<!DOCTYPE html>
<html lang="en">
<head>
<meta charset="utf-8">
<title>Bureau Ostrelle – Report Cover</title>
<link href="https://fonts.googleapis.com/css2?family=Montserrat:wght@500;700;800&display=swap" rel="stylesheet">
<style>
  :root {
    --brand-red: #c8000f;
    --brand-red-deep: #a3000a;
    --brand-red-bright: #d90a16;
    --text-light: #ffffff;
    --fire-dark: #3a1408;
    --fire-mid: #b8430f;
    --fire-hot: #f39a1e;
    --fire-glow: #ffd56a;
  }
  * { margin: 0; padding: 0; box-sizing: border-box; }
  html, body {
    width: 846px;
    height: 1200px;
    overflow: hidden;
    background: var(--brand-red);
  }
  .cover {
    position: relative;
    width: 846px;
    height: 1200px;
    overflow: hidden;
    background: linear-gradient(180deg, var(--brand-red-deep) 0%, var(--brand-red) 45%, var(--brand-red-bright) 100%);
    font-family: "Montserrat", Arial, sans-serif;
    color: var(--text-light);
  }
  .brand {
    position: absolute;
    top: 86px;
    right: 90px;
    display: flex;
    align-items: center;
    gap: 20px;
  }
  .brand-mark {
    width: 60px;
    height: 60px;
    border-radius: 50%;
    background: var(--text-light);
  }
  .brand-name {
    font-weight: 500;
    font-size: 42px;
    line-height: 1.08;
    letter-spacing: -0.5px;
  }
  .project-heading {
    position: absolute;
    top: 224px;
    right: 40px;
    text-align: right;
  }
  .project-title {
    font-weight: 800;
    font-size: 53px;
    line-height: 1.1;
    letter-spacing: 0.2px;
  }
  .project-subtext {
    margin-top: 18px;
    font-weight: 500;
    font-size: 39px;
    line-height: 1.1;
  }
  .cover-photo {
    position: absolute;
    left: 20px;
    top: 372px;
    width: 826px;
    height: 828px;
    border-radius: 180px 180px 0 0;
    background:
      radial-gradient(ellipse 55% 45% at 50% 60%, var(--fire-glow) 0%, var(--fire-hot) 30%, transparent 70%),
      linear-gradient(180deg, var(--fire-dark) 0%, var(--fire-mid) 45%, var(--fire-hot) 100%);
  }
</style>
</head>
<body>
  <main class="cover">
    <header class="brand">
      <span class="brand-mark"></span>
      <span class="brand-name">Bureau<br>Ostrelle</span>
    </header>

    <section class="project-heading">
      <h1 class="project-title">PROJECT TITLE HERE</h1>
      <p class="project-subtext">Subtext here</p>
    </section>

    <div class="cover-photo" role="img" aria-label="Photograph of a tall building engulfed in fire at night"></div>
  </main>
</body>
</html>
```